Flyer-Design
Zielgruppe
Ich bin gelernte Bankkauffrau, Dipl. Betriebswirtin, geprüfte Immobilienberaterin sowie Bausachverständige für Immobilienbewertung. Nach mehr als 30 Jahren Tätigkeit als Immobilienmaklerin für diverse Banken und große Maklerunternehmen, habe ich zum 01.01.2022 meine eigene Firma, die Tarvo Immobilienberatung GmbH & Co. KG gegründet.
Da Großunternehmen sehr unflexibel und träge sind und man dadurch nicht auf alle Bedürfnisse des Kunden so eingehen kann, wie ich es mir für meine Kunden wünsche, habe ich meine eigene Firma gegründet. Überschaubar groß, flexibel und Kundennah. Bei uns steht der Mensch mit all seinen Emotionen rund um den Immobilienverkauf im Vordergrund.
Wir bieten zusätzlich zum klassischen rundum-sorglos Immobilienverkauf von Bestandsimmobilien, auch Honorarberatung für Immobilien Selbstverkäufer an. Darüber hinaus auch Baufinanzierungen.
Unsere Zielgruppe sind verkaufsbereite Immobilieneigentümer jeglichen Alters. Meistens sind die Verkäufer jedoch im fortgeschrittenen Alter. Sowie Immobilienkäufer, die eine Finanzierung benötigen.
Aufgabenstellung
Er soll zum Design unserer Homepage passen www.tarvo-immobilien-beispiel.de.
Die Flyer sollen zum Auslegen, zur Mitnahme aus Hängeboxen und zum Briefkasteneinwurf dienen, um unsere Firma bekannt zu machen und Aufträge zu generieren.
Modern, aber nicht zu flippig/unruhig. Er muss die ältere Generation mit Bild und Text emotional ansprechen und Sicherheit vermitteln, aber auch die 30-40 Jährigen. Er soll sich von den üblichen, langweiligen Maklerflyern abheben.
Den Flyer wünschen wir uns später auch in DIN A4 Format zur Übergabe beim Kunden in einer Mappe.

```html
<!DOCTYPE html>
<html lang="de">
<head>
<meta charset="utf-8">
<title>Tarvo Immobilienberatung – Flyer</title>
<link rel="stylesheet" href="https://fonts.googleapis.com/css2?family=Raleway:wght@400;500;600;700;800&display=swap">
<style>
  :root{
    --navy:#23305f;
    --navy-dark:#1b2550;
    --tan:#b59c79;
    --tan-light:#cdb99b;
    --cream:#f3eee7;
    --paper:#ffffff;
    --stage:#eceef1;
    --text:#2b2f45;
  }
  *{box-sizing:border-box;margin:0;padding:0}
  html,body{width:1200px;height:847px;overflow:hidden;background:var(--stage);font-family:"Raleway",sans-serif;color:var(--text)}
  .canvas{position:relative;width:1200px;height:847px}
  .flyer{position:absolute;top:91px;width:470px;height:720px;background:var(--paper);overflow:hidden;box-shadow:0 6px 18px rgba(30,35,60,.18)}
  .flyer--front{left:113px}
  .flyer--back{left:629px}
  .layer{position:absolute;inset:0}
  .photo{position:absolute}

  /* front */
  .brand-block{position:absolute;left:0;top:0;width:178px;height:222px;background:rgba(181,156,121,.88);padding:48px 0 0 22px;color:#fff}
  .brand-name{font-size:36px;font-weight:700;letter-spacing:2px;line-height:1}
  .brand-sub{font-size:7px;letter-spacing:1.6px;margin-top:5px;opacity:.9}
  .claim-block{position:absolute;left:0;top:222px;width:178px;height:140px;background:rgba(255,255,255,.82);padding:18px 0 0 22px}
  .claim{font-size:15px;font-weight:700;color:var(--navy);line-height:1.2;text-transform:uppercase}
  .intro{position:absolute;right:24px;top:492px;width:245px;text-align:justify;text-align-last:right;font-size:12.5px;line-height:1.45;color:var(--text)}
  .slogan{position:absolute;right:22px;top:596px;display:flex;align-items:flex-end;gap:10px}
  .slogan-lead{font-size:15px;color:var(--tan);line-height:1.15;text-align:right}
  .slogan-lead b{color:var(--navy);font-weight:700;font-size:20px}
  .slogan-word{font-size:38px;font-weight:800;color:var(--tan);letter-spacing:1px;line-height:1}
  .property-bar{position:absolute;left:0;bottom:0;width:100%;height:64px;background:var(--navy);display:flex;justify-content:space-around;align-items:center;padding:0 18px}
  .property-type{display:flex;flex-direction:column;align-items:center;gap:4px;color:#fff;font-size:7px}
  .property-type svg{width:22px;height:22px}

  /* back */
  .logo{position:absolute;left:22px;top:22px;display:flex;align-items:center;gap:6px}
  .logo-mark{width:12px;height:12px;background:var(--tan);border-radius:50%}
  .logo-name{font-size:16px;font-weight:700;color:var(--navy);letter-spacing:1.5px}
  .headline{position:absolute;left:200px;top:58px;width:250px;text-align:center;font-size:24px;font-weight:800;line-height:1.2;color:var(--navy)}
  .benefits{position:absolute;left:282px;top:236px;width:180px;color:#fff;font-size:17px;line-height:1.3;list-style:none}
  .benefits li{padding-left:12px;position:relative}
  .benefits li::before{content:"";position:absolute;left:0;top:9px;width:5px;height:5px;border-radius:50%;background:#fff}
  .cta{position:absolute;left:200px;top:338px;width:250px;height:22px;background:var(--tan);color:#fff;font-size:9px;font-weight:700;letter-spacing:.8px;display:flex;align-items:center;justify-content:center}
  .web{position:absolute;left:110px;top:494px;font-size:18px;font-weight:700;color:var(--navy)}
  .contact-bar{position:absolute;left:0;bottom:0;width:100%;height:62px;background:var(--navy);display:flex;align-items:center;justify-content:space-between;padding:0 20px;color:#fff;font-size:8px}
  .contact-item{display:flex;align-items:center;gap:6px}
  .contact-item svg{width:13px;height:13px;flex:none}
</style>
</head>
<body>
<div class="canvas">

  <!-- Front page -->
  <section class="flyer flyer--front">
    <svg class="layer" viewBox="0 0 470 720" aria-hidden="true">
      <defs>
        <linearGradient id="roomTone" x1="0" y1="0" x2="1" y2="1">
          <stop offset="0" stop-color="#e9e4dc"/>
          <stop offset=".55" stop-color="#cfc5b7"/>
          <stop offset="1" stop-color="#8a7563"/>
        </linearGradient>
        <linearGradient id="deskTone" x1="0" y1="0" x2="1" y2="1">
          <stop offset="0" stop-color="#dfe2e6"/>
          <stop offset="1" stop-color="#a9b0ba"/>
        </linearGradient>
      </defs>
      <polygon points="0,0 470,0 470,360 0,560" fill="url(#deskTone)"/>
      <polygon points="0,0 470,0 470,360 178,484 178,360 0,360" fill="url(#roomTone)"/>
      <polygon points="0,430 178,370 178,484 0,560" fill="var(--navy)"/>
      <polygon points="0,560 470,360 470,372 0,572" fill="var(--tan-light)"/>
      <polygon points="0,572 470,372 470,720 0,720" fill="var(--paper)"/>
    </svg>
    <div class="photo" role="img" aria-label="Foto eines hellen, modern eingerichteten Wohnzimmers mit Sofa und Holztisch" style="left:178px;top:0;width:292px;height:360px"></div>
    <div class="photo" role="img" aria-label="Foto eines Schreibtischs mit Unterlagen und Tablet" style="left:0;top:360px;width:178px;height:200px"></div>

    <div class="brand-block">
      <div class="brand-name">TARVO</div>
      <div class="brand-sub">IMMOBILIENBERATUNG</div>
    </div>
    <div class="claim-block">
      <p class="claim">Ihr Immobilienprofi<br>für<br>Rhein-Neckar<br>und die Pfalz</p>
    </div>

    <p class="intro">Egal ob Sie Ihre Immobilie ohne Makler verkaufen oder sich lieber entspannt zurücklehnen und unseren Rundum-sorglos Service nutzen wollen …</p>

    <div class="slogan">
      <p class="slogan-lead">Bei uns <b>sind Sie</b><br>in jedem Fall</p>
      <p class="slogan-word">RICHTIG</p>
    </div>

    <div class="property-bar">
      <div class="property-type">
        <svg viewBox="0 0 24 24" fill="none" stroke="#fff" stroke-width="1.6"><path d="M3 11 12 4l9 7"/><path d="M5 10v10h14V10"/><path d="M10 20v-5h4v5"/></svg>
        <span>Haus</span>
      </div>
      <div class="property-type">
        <svg viewBox="0 0 24 24" fill="none" stroke="#fff" stroke-width="1.6"><rect x="4" y="3" width="10" height="18"/><rect x="14" y="9" width="6" height="12"/><path d="M7 7h1M10 7h1M7 11h1M10 11h1M7 15h1M10 15h1"/></svg>
        <span>Mehrfamilienhaus</span>
      </div>
      <div class="property-type">
        <svg viewBox="0 0 24 24" fill="none" stroke="#fff" stroke-width="1.6"><rect x="6" y="3" width="12" height="18"/><path d="M9 7h2M13 7h2M9 11h2M13 11h2M11 21v-4h2v4"/></svg>
        <span>Wohnung</span>
      </div>
      <div class="property-type">
        <svg viewBox="0 0 24 24" fill="none" stroke="#fff" stroke-width="1.6"><path d="M3 18h18M5 18V9M9 18V9M13 18V9M17 18V9M3 11h18"/></svg>
        <span>Grundstücksfläche</span>
      </div>
    </div>
  </section>

  <!-- Back page -->
  <section class="flyer flyer--back">
    <svg class="layer" viewBox="0 0 470 720" aria-hidden="true">
      <defs>
        <linearGradient id="handsTone" x1="0" y1="0" x2="1" y2="1">
          <stop offset="0" stop-color="#eadfd2"/>
          <stop offset="1" stop-color="#b89c82"/>
        </linearGradient>
        <linearGradient id="lakeTone" x1="0" y1="0" x2="0" y2="1">
          <stop offset="0" stop-color="#e6d7bd"/>
          <stop offset=".5" stop-color="#c7b79c"/>
          <stop offset="1" stop-color="#6f6a68"/>
        </linearGradient>
      </defs>
      <polygon points="0,125 200,125 200,300 0,360" fill="url(#handsTone)"/>
      <polygon points="0,420 280,228 470,170 470,375 0,470" fill="var(--navy)"/>
      <polygon points="0,470 470,375 470,392 0,487" fill="var(--tan-light)"/>
      <polygon points="0,560 470,525 470,660 0,660" fill="url(#lakeTone)"/>
    </svg>
    <div class="photo" role="img" aria-label="Foto von Händen, die ein kleines Holzhaus halten" style="left:0;top:125px;width:200px;height:200px"></div>
    <div class="photo" role="img" aria-label="Foto eines Paares auf einem Steg am See bei Sonnenuntergang" style="left:0;top:525px;width:470px;height:135px"></div>

    <div class="logo">
      <span class="logo-mark"></span>
      <span class="logo-name">TARVO</span>
    </div>

    <h1 class="headline">KENNEN SIE<br>DEN WERT<br>IHRER IMMOBILIE?</h1>

    <ul class="benefits">
      <li>Kostenfrei &amp; unverbindlich</li>
      <li>Schnell &amp; einfach</li>
      <li>Direktes Ergebnis</li>
    </ul>

    <div class="cta">JETZT ONLINE MARKTWERT ERMITTELN</div>

    <p class="web">www.tarvo-immobilien-beispiel.de</p>

    <div class="contact-bar">
      <div class="contact-item">
        <svg viewBox="0 0 24 24" fill="#fff"><path d="M6.6 10.8a15 15 0 0 0 6.6 6.6l2.2-2.2a1 1 0 0 1 1-.25 11 11 0 0 0 3.6.6 1 1 0 0 1 1 1V20a1 1 0 0 1-1 1A17 17 0 0 1 3 4a1 1 0 0 1 1-1h3.5a1 1 0 0 1 1 1 11 11 0 0 0 .6 3.6 1 1 0 0 1-.25 1z"/></svg>
        <span>0621 / 000 1100</span>
      </div>
      <div class="contact-item">
        <svg viewBox="0 0 24 24" fill="none" stroke="#fff" stroke-width="2"><rect x="3" y="5" width="18" height="14"/><path d="m3 6 9 7 9-7"/></svg>
        <span>kontaktpl3@tarvo-immobilien-beispiel.de</span>
      </div>
      <div class="contact-item">
        <svg viewBox="0 0 24 24" fill="#fff"><path d="M12 2a7 7 0 0 0-7 7c0 5 7 13 7 13s7-8 7-13a7 7 0 0 0-7-7zm0 9.5A2.5 2.5 0 1 1 12 6.5a2.5 2.5 0 0 1 0 5z"/></svg>
        <span>Musterweg 12<br>68000 Beispielstadt</span>
      </div>
    </div>
  </section>

</div>
</body>
</html>
```